Brell Harbor Company Business Cards

Front and Back Business Card - logo and text setup - cool design. I need workable photoshop or illustrator files so I can setup each employee card with design that is created
Updates

Hi everyone, thank you for the great entries. Please no more white and blue cards - there are so many already - black and silver only now please. thanks!

Target Market(s)

Construction Industry - Facility Managers

Industry/Entity Type

Construction

Contact Information for Business Card

I really like contemporary simplistic looks - clean neat....not opposed to seeing some black backrounds

Requirements
Must have
• Logo/website address with design on front only - www.brellharbor-example.com (logo attached)
• Back:
• Name/Title/Company Address/Phone/email address
Nice to have
• Cool design
Should not have
• Nothing gimmicky like Fire or Water - since we are a Fire Protection company - it has all been done

```html
<!DOCTYPE html>
<html lang="en">
<head>
<meta charset="utf-8">
<title>Brell Harbor Company – Business Cards</title>
<link href="https://fonts.googleapis.com/css2?family=Open+Sans:wght@400;600;700&display=swap" rel="stylesheet">
<style>
  :root{
    --page:#c5d0d0;
    --card-dark:#2e3438;
    --panel:#a9b8bb;
    --bar:#d6dfe0;
    --silver-light:#e9ecee;
    --silver-mid:#b9bfc3;
    --silver-dark:#8e969b;
    --ink:#1c1f22;
    --brand:#1f3f95;
    --icon:#2f8ff0;
    --white:#ffffff;
  }
  *{box-sizing:border-box;margin:0;padding:0}
  html,body{width:1200px;height:1000px;overflow:hidden}
  body{background:var(--page);font-family:"Open Sans",Arial,sans-serif;position:relative}
  .card{position:absolute;left:250px;width:700px;height:400px;border-radius:34px;overflow:hidden;background:var(--card-dark);box-shadow:0 10px 24px rgba(0,0,0,.25)}
  .card--front{top:60px}
  .card--back{top:530px}

  /* front */
  .front__seal{position:absolute;left:50px;top:75px;width:260px;height:260px;border-radius:50%;
    background:linear-gradient(135deg,var(--silver-light) 0%,var(--silver-mid) 55%,var(--silver-dark) 100%);
    display:flex;align-items:center;justify-content:center}
  .brand-name{font-weight:700;color:var(--brand);font-size:32px;letter-spacing:-.5px;white-space:nowrap}
  .front__web{position:absolute;left:345px;top:178px;color:var(--white);font-size:25px;letter-spacing:.3px}

  /* back */
  .back__shapes{position:absolute;inset:0}
  .back__band{position:absolute;left:470px;top:60px;width:230px;height:62px;
    background:linear-gradient(90deg,var(--silver-dark) 0%,var(--silver-light) 45%,var(--silver-mid) 100%);
    display:flex;align-items:center;justify-content:center}
  .back__band .brand-name{font-size:26px}
  .person{position:absolute;left:70px;top:118px;color:var(--ink)}
  .person__name{font-weight:700;font-size:25px;line-height:1.2}
  .person__title{font-size:22px;line-height:1.2}
  .contact{position:absolute;left:66px;top:200px;list-style:none}
  .contact__item{display:flex;align-items:center;height:34px;margin-bottom:12px}
  .contact__icon{width:32px;height:32px;border-radius:9px;background:var(--icon);display:flex;align-items:center;justify-content:center;margin-right:26px}
  .contact__text{font-size:22px;color:var(--ink)}
</style>
</head>
<body>

<section class="card card--front" aria-label="Business card front">
  <div class="front__seal"><span class="brand-name">Brell Harbor</span></div>
  <p class="front__web">www.brellharbor-example.com</p>
</section>

<section class="card card--back" aria-label="Business card back">
  <svg class="back__shapes" width="700" height="400" viewBox="0 0 700 400">
    <defs>
      <clipPath id="panel-clip"><path d="M0 0 H400 Q590 200 480 400 H0 Z"/></clipPath>
    </defs>
    <path d="M0 0 H400 Q590 200 480 400 H0 Z" fill="var(--panel)"/>
    <g clip-path="url(#panel-clip)" fill="var(--bar)">
      <rect x="250" y="60" width="400" height="34"/>
      <rect x="250" y="106" width="400" height="34"/>
      <rect x="250" y="152" width="400" height="34"/>
      <rect x="124" y="200" width="520" height="34" rx="6"/>
      <rect x="124" y="246" width="520" height="34" rx="6"/>
      <rect x="124" y="292" width="520" height="34" rx="6"/>
      <rect x="124" y="338" width="520" height="34" rx="6"/>
    </g>
  </svg>

  <div class="back__band"><span class="brand-name">Brell Harbor</span></div>

  <div class="person">
    <p class="person__name">Personal Name</p>
    <p class="person__title">Title</p>
  </div>

  <ul class="contact">
    <li class="contact__item">
      <span class="contact__icon"><svg width="18" height="18" viewBox="0 0 24 24"><path fill="#fff" d="M6.6 10.8a15 15 0 0 0 6.6 6.6l2.2-2.2a1 1 0 0 1 1-.25 11.4 11.4 0 0 0 3.6.57 1 1 0 0 1 1 1V20a1 1 0 0 1-1 1A17 17 0 0 1 3 4a1 1 0 0 1 1-1h3.5a1 1 0 0 1 1 1c0 1.25.2 2.45.57 3.57a1 1 0 0 1-.25 1z"/></svg></span>
      <span class="contact__text">0123456789</span>
    </li>
    <li class="contact__item">
      <span class="contact__icon"><svg width="18" height="14" viewBox="0 0 24 18"><rect x="1" y="1" width="22" height="16" rx="2" fill="#fff"/><path d="M2 2 L12 10 L22 2" stroke="var(--icon)" stroke-width="2" fill="none"/></svg></span>
      <span class="contact__text">Email address</span>
    </li>
    <li class="contact__item">
      <span class="contact__icon"><svg width="18" height="18" viewBox="0 0 24 24" fill="none" stroke="#fff" stroke-width="2"><circle cx="12" cy="12" r="10"/><ellipse cx="12" cy="12" rx="4.5" ry="10"/><path d="M2 12h20M4 7h16M4 17h16"/></svg></span>
      <span class="contact__text">www.brellharbor-example.com</span>
    </li>
    <li class="contact__item">
      <span class="contact__icon"><svg width="16" height="20" viewBox="0 0 20 26"><path fill="#fff" d="M10 0a10 10 0 0 0-10 10c0 7.5 10 16 10 16s10-8.5 10-16A10 10 0 0 0 10 0z"/><circle cx="10" cy="10" r="3.5" fill="var(--icon)"/></svg></span>
      <span class="contact__text">Company Address</span>
    </li>
  </ul>
</section>

</body>
</html>
```